Maren Spacial\floral Decorator

Maren is a spacial\floral decorator. She is passionate about Art, Life, Architecture, Painting, Music and movement. Her website will be used to showcase her spacial and floral design projects.
We are looking for a very unique website that stands apart from the crowd.
We believe that is achieved through simple high quality design Simple being very important.
The Home page should display primarily photos.
Your task is to provide an un-coded homepage template.
The page must be dynamic in its style and feel.

Maren has suggest a grid pattern for the images, similar to this http://www.dovelmarchblooms.co.uk. Overall We like the look and feel of this site.

We like the following color palettes, please base your design around one of them;
https://tintvault.example.com/#themes/search?term=5519047
https://tintvault.example.com/#themes/search?term=5513628
https://tintvault.example.com/#themes/search?term=5527154
https://tintvault.example.com/#themes/search?term=5518462
https://tintvault.example.com/#themes/search?term=5514309

Our target Market is High End Corporate Clients, located in Shanghai and Taipai. For these clients she utilise her floral and interior design skills to decorate a space. See Photos 2, 3 and 21 for examples.
She also targets High End personal clients for events such as weddings and gift combination i.e. flowers and something else.

Industry/Entity Type

Floral

Requirements
Must have
• Chinese/ English Language Selection
A selection of pictures that appear and disappear.
A menu system that includes:
Home – Portfolio – About Maren – Blog – Contact Her
A very subtle menu system linking to chatterbox, workbridge Up, q* and zhuta.
Nice to have
• We also like the use of an image for the background but this is not necessary.
Should not have
• Alot of Text, yes we now this isn't great for SEO but we will deal with that on other pages

```html
<!DOCTYPE html>
<html lang="en">
<head>
<meta charset="utf-8">
<title>Maren — spacial &amp; floral decorator</title>
<link href="https://fonts.googleapis.com/css2?family=Jost:wght@200;300;400&display=swap" rel="stylesheet">
<style>
  :root {
    --paper: #f9fafb;
    --nav-muted: #c9cccd;
    --nav-sage: #8fa9a1;
    --ink: #555a5c;
    --wordmark: #8a8a8a;
    --hero-plum: #8a3f7e;
    --hero-rose: #c1689e;
    --hero-lime: #b9c46a;
    --hero-violet: #5a3a7a;
    --hero-text: #f3eef2;
    --social-bg: #c9928b;
    --social-text: #fbf4f2;
    --rule: #e6e8e9;
    --footnote: #7b7f81;
  }
  * { margin: 0; padding: 0; box-sizing: border-box; }
  html, body {
    width: 1200px; height: 1000px; overflow: hidden;
    background: var(--paper);
    font-family: "Jost", sans-serif;
  }
  .page { position: relative; width: 1200px; height: 1000px; }

  .main-nav a {
    position: absolute; text-decoration: none; font-weight: 300;
  }
  .nav-home { left: 300px; top: 162px; font-size: 33px; color: var(--nav-muted); font-weight: 300; }
  .nav-about { left: 462px; top: 174px; font-size: 18px; color: var(--nav-sage); }
  .nav-contact { left: 622px; top: 174px; font-size: 18px; color: var(--nav-sage); }

  .language-switch {
    position: absolute; left: 915px; top: 180px;
    font-size: 14px; font-weight: 300; color: var(--ink); letter-spacing: 0.3px;
  }
  .language-switch .divider { margin: 0 6px; color: #222; font-weight: 400; }

  .hero {
    position: absolute; left: 300px; top: 200px; width: 597px; height: 598px;
    background:
      radial-gradient(circle at 72% 30%, var(--hero-lime) 0 8%, transparent 18%),
      radial-gradient(circle at 15% 45%, var(--hero-lime) 0 6%, transparent 16%),
      radial-gradient(circle at 58% 48%, var(--hero-rose) 0 10%, transparent 26%),
      radial-gradient(circle at 80% 88%, var(--hero-violet) 0 8%, transparent 20%),
      linear-gradient(160deg, var(--hero-rose), var(--hero-plum) 55%, var(--hero-rose));
  }
  .hero-cta {
    position: absolute; left: 300px; top: 234px; width: 597px; text-align: center;
    font-size: 46px; color: var(--hero-text); text-decoration: none; letter-spacing: 0.5px;
  }
  .hero-cta .light { font-weight: 200; }
  .hero-cta .strong { font-weight: 400; }

  .wordmark {
    position: absolute; left: 318px; top: 540px;
    font-size: 232px; font-weight: 200; color: var(--wordmark);
    letter-spacing: -6px; line-height: 1;
  }

  .online-label {
    position: absolute; left: 913px; top: 616px;
    font-size: 18px; font-weight: 300; color: var(--nav-sage);
  }
  .social-links {
    position: absolute; left: 913px; top: 646px; width: 137px; height: 152px;
    background: var(--social-bg); list-style: none; padding-top: 12px;
  }
  .social-links li {
    display: flex; justify-content: flex-end; align-items: center;
    height: 35px; padding-right: 10px;
  }
  .social-links a {
    color: var(--social-text); text-decoration: none; font-size: 13px; font-weight: 400;
    margin-right: 10px; white-space: nowrap;
  }
  .social-links .mark { width: 26px; height: 26px; border: 2px solid var(--social-text); }

  .footer-rule {
    position: absolute; left: 250px; top: 852px; width: 680px; height: 1px; background: var(--rule);
  }
  .footer-note {
    position: absolute; left: 300px; top: 855px; width: 600px; text-align: center;
    font-size: 10px; line-height: 10px; color: var(--footnote); font-weight: 300;
  }
</style>
</head>
<body>
<div class="page">
  <nav class="main-nav">
    <a class="nav-home" href="#">home</a>
    <a class="nav-about" href="#">about maren</a>
    <a class="nav-contact" href="#">contact her</a>
  </nav>

  <div class="language-switch"><span>chinese</span><span class="divider">|</span><span>english</span></div>

  <div class="hero" role="img" aria-label="Photograph of a lush floral arrangement with irises, lilac, hydrangea and lime-green blooms"></div>
  <a class="hero-cta" href="#"><span class="light">view </span><span class="strong">portfolio</span></a>

  <div class="wordmark">maren</div>

  <div class="online-label">online</div>
  <ul class="social-links">
    <li><a href="#">Chatterbox</a><span class="mark"></span></li>
    <li><a href="#">Workbridge Up</a><span class="mark"></span></li>
    <li><a href="#">q*</a><span class="mark"></span></li>
    <li><a href="#">zhuta</a><span class="mark"></span></li>
  </ul>

  <div class="footer-rule"></div>
  <p class="footer-note">Aliquam sit amet ultricies lectus. Mauris at diam quis sem hendrerit dictum. Etiam consequat mauris at tellus viverra auctor. Phasellus sit amet neque ante. Suspendisse dignissim luctus sapien, nec ultrices metus rhoncus ut. Nulla non mauris arcu.</p>
</div>
</body>
</html>
```